Aircraft maintenance buisness card

I am an aircraft mechanic looking for a personal buisness card . I would like my name and a title of Aircraft Maintenance Manager . I would like a suttle picture of an aircraft and helicopter .

elegant and professional wtih my contact .

My name should be on the car and Aircraft Maintenance Manager under with my contact infor below .

i have attached some pictures but i am open to other pics and ideas . I would like a airliner or private jet and a helicopter in the picture . The Images should be suttle and not the main idea . I also uploaded a picture of a jet engine which is cool . Be creative and i will work with you to finalize something .
Updates

Project Deadline Extended
Reason: Looking for more variations . Very good so far but looiking for a bit more styles and i uploaded my logo that i purchased . Please use my logo and be creative with it . I like some variations of black card with maybe some pictures that i uploaded but i am open to ideas . Be creative and i will work with you .

Project Deadline Extended
Reason: Looking for more designs and variations . Not yet satisfied with the designs i have gotten .

Industry/Entity Type

Aviation

Contact Information for Business Card

Aircraft Maintenance Manager

Font styles to use
Serif

Colors

Designer to choose colors to be used in the design.

Requirements
Must have
• An aviation related Logo if possible incorporated in the card possibly
• My name
• Tiberio Malvade Furtunato
• 482 Pellow St.
• Kearny , NJ
• 08519
• Email: Lwskyfixtech@mailvora.com
Nice to have
• Suttle Backround of a Private Jet or Airliner and a Helicopter .

```html
<!DOCTYPE html>
<html lang="en">
<head>
<meta charset="utf-8">
<title>Tiberio Malvade Furtunato – Business Card</title>
<link href="https://fonts.googleapis.com/css2?family=Cormorant+SC:wght@400;500&family=Jost:wght@400;600&display=swap" rel="stylesheet">
<style>
  :root {
    --stage: #2a2a2c;
    --card-dark: #242426;
    --card-dark-pattern: #2c2c2e;
    --emboss: #505054;
    --emboss-light: #5c5c60;
    --card-light: #f5f5f6;
    --brand-blue: #1f4fa8;
    --ink: #2b2b2e;
    --muted: #55565a;
  }
  * { margin: 0; padding: 0; box-sizing: border-box; }
  html, body { width: 1200px; height: 900px; overflow: hidden; }
  body { background: var(--stage); position: relative; }

  .card {
    position: absolute;
    left: 290px;
    width: 620px;
    height: 354px;
    box-shadow: 0 10px 30px rgba(0,0,0,.45);
  }

  /* Back */
  .card-back { top: 50px; background: var(--card-dark); overflow: hidden; }
  .card-back .pattern {
    position: absolute; inset: 0;
    background: radial-gradient(ellipse at center, var(--card-dark-pattern), var(--card-dark));
  }
  .card-back .identity {
    position: absolute; left: 0; right: 0; top: 130px; text-align: center;
    font-family: "Cormorant SC", serif;
  }
  .card-back .name {
    font-size: 36px; font-weight: 500; letter-spacing: 2px;
    color: var(--emboss-light);
    text-shadow: 0 1px 0 rgba(255,255,255,.08), 0 -1px 0 rgba(0,0,0,.6);
  }
  .card-back .title {
    margin-top: 2px; font-size: 17px; letter-spacing: 1.5px;
    color: var(--emboss);
    text-shadow: 0 -1px 0 rgba(0,0,0,.6);
  }

  /* Front */
  .card-front { top: 470px; background: var(--card-light); }
  .card-front .accent-bar {
    position: absolute; left: 0; top: 48px; width: 8px; height: 46px; background: var(--brand-blue);
  }
  .card-front .identity { position: absolute; left: 32px; top: 46px; }
  .card-front .name {
    font-family: "Jost", sans-serif; font-weight: 600; font-size: 25px;
    letter-spacing: .5px; text-transform: uppercase; color: var(--brand-blue);
  }
  .card-front .title {
    font-family: "Cormorant SC", serif; font-size: 18px; letter-spacing: 1px; color: var(--muted);
    margin-top: -2px;
  }

  .brand {
    position: absolute; right: 48px; top: 122px;
    display: flex; align-items: center; gap: 10px;
  }
  .brand .mark { width: 26px; height: 26px; background: var(--brand-blue); }
  .brand .brand-name {
    font-family: "Jost", sans-serif; font-weight: 600; font-size: 22px; color: var(--brand-blue);
    letter-spacing: .5px;
  }

  .contact { position: absolute; left: 32px; top: 226px; list-style: none; }
  .contact li {
    display: flex; align-items: center; gap: 14px; height: 30px;
    font-family: "Jost", sans-serif; font-size: 17px; color: var(--ink); letter-spacing: .6px;
  }
  .contact svg { width: 18px; height: 18px; stroke: var(--muted); fill: none; stroke-width: 1.4; }

  .address {
    position: absolute; right: 48px; bottom: 28px;
    font-family: "Jost", sans-serif; font-size: 18px; line-height: 1.3; color: var(--ink);
    font-style: normal;
  }
</style>
</head>
<body>

<section class="card card-back">
  <div class="pattern" role="img" aria-label="Faint repeating pattern of small aircraft and helicopter silhouettes"></div>
  <div class="identity">
    <p class="name">Tiberio Malvade Furtunato</p>
    <p class="title">Aircraft Maintenance Manager</p>
  </div>
</section>

<section class="card card-front">
  <div class="accent-bar"></div>
  <div class="identity">
    <p class="name">Tiberio Malvade Furtunato</p>
    <p class="title">Aircraft Maintenance Manager</p>
  </div>

  <div class="brand">
    <span class="mark"></span>
    <span class="brand-name">Skyfix Aviation</span>
  </div>

  <ul class="contact">
    <li>
      <svg viewBox="0 0 24 24"><path d="M5 3h4l2 5-2.5 1.5a11 11 0 0 0 6 6L16 13l5 2v4a2 2 0 0 1-2 2A16 16 0 0 1 3 5a2 2 0 0 1 2-2z"/></svg>
      614-555-0148
    </li>
    <li>
      <svg viewBox="0 0 24 24"><rect x="3" y="5" width="18" height="14"/><path d="M3 5l9 8 9-8"/></svg>
      tiberio@skyfixtechaviation.com
    </li>
    <li>
      <svg viewBox="0 0 24 24"><circle cx="12" cy="12" r="9"/><path d="M3 12h18M12 3c3 3 3 15 0 18M12 3c-3 3-3 15 0 18"/></svg>
      skyfixtechaviation.com
    </li>
  </ul>

  <address class="address">482 Pellow St.<br>Belmar Ridge, OH, 08519</address>
</section>

</body>
</html>
```